New Website for NY and South Florida Based Accounting Firm

Accounting and Audit firm located in New York and South Florida needs a website redesign after acquiring new businesses and adding new services.

Our current website can be found here:
http://www.trqbnllp.example/

We have merged with this firm:
http://hollisbarkerwendtfield.example/

We are looking for a comprehensive design that will highlight the firm's dual locations. The final design should communicate security, strength, and growth. We would like to keep our pyramid logo as seen on the trqbnllp.example website, as this has been our logo for over 20 years.

Industry/Entity Type

Accounting

Number of Pages Required

1 page

Font styles to use
Serif
Sans Serif

```html
<!DOCTYPE html>
<html lang="en">
<head>
<meta charset="utf-8">
<title>Tarrow, Quell, Bancroft &amp; Nilsen, LLP</title>
<link href="https://fonts.googleapis.com/css2?family=Raleway:wght@500;600;700&family=Roboto:wght@300;400;500&family=Libre+Baskerville&display=swap" rel="stylesheet">
<style>
:root{
  --gold:#e8ad00;
  --gold-text:#e3a20f;
  --ink:#333;
  --muted:#8a8a8a;
  --light:#b0b0b0;
  --line:#d6d6d6;
  --footer:#262626;
  --white:#fff;
}
*{margin:0;padding:0;box-sizing:border-box}
html,body{width:726px;height:1200px;overflow:hidden;background:var(--white);font-family:'Roboto',sans-serif;color:var(--ink)}
.page{position:relative;width:726px;height:1200px}
.hero{position:absolute;left:0;top:0;width:726px;height:342px;overflow:hidden}
.hero-photo{position:absolute;inset:0;background:linear-gradient(90deg,#f4f2ef 0%,#ece9e5 40%,#b7b8bc 62%,#3b4150 80%,#8d8a88 100%)}
.hero-shade{position:absolute;inset:0;background:linear-gradient(180deg,rgba(255,255,255,0) 60%,rgba(60,60,70,.25) 100%)}
.brand{position:absolute;left:74px;top:20px;width:104px;text-align:center;font-family:'Libre Baskerville',serif;font-size:7px;line-height:10px;color:#222;font-variant:small-caps}
.brand-mark{display:block;width:12px;height:12px;margin:0 auto 18px;background:var(--gold)}
.nav{position:absolute;top:24px;left:264px;display:flex;gap:0;font-size:7.5px;font-weight:500;color:var(--white);letter-spacing:.1px}
.nav a{color:#fff;text-decoration:none;margin-right:16px}
.nav a.active{color:var(--gold)}
.hero-copy{position:absolute;left:79px;top:112px;width:320px}
.hero-title{font-family:'Raleway',sans-serif;font-weight:700;font-size:24px;color:var(--gold-text);letter-spacing:.2px}
.hero-lead{font-family:'Libre Baskerville',serif;font-size:11.6px;line-height:17px;color:#222;margin-top:8px;letter-spacing:-.2px}
.hero-body{font-size:7.3px;line-height:13px;color:#444;margin-top:10px;width:310px}
.btn-outline{display:inline-block;margin-top:13px;border:1px solid var(--gold);border-radius:3px;padding:6px 8px;font-family:'Raleway',sans-serif;font-size:7.5px;font-weight:700;color:var(--gold-text)}
.slider-arrows{position:absolute;left:670px;top:300px}
.section-title{font-family:'Raleway',sans-serif;font-weight:500;font-size:13px;letter-spacing:.6px;text-align:center;color:#333}
.section-title span{color:var(--gold-text)}
.section-intro{font-size:7.8px;line-height:14.5px;color:var(--muted);text-align:center;margin-top:12px}
.services{position:absolute;top:342px;left:0;width:726px;height:254px}
.services .section-title{margin-top:34px}
.service{position:absolute;top:106px;width:130px;text-align:center}
.service-icon{width:57px;height:57px;border:1px solid #bbb;border-radius:50%;margin:0 auto;display:flex;align-items:center;justify-content:center}
.service h3{font-family:'Raleway',sans-serif;font-size:7.6px;font-weight:600;color:var(--gold-text);margin-top:12px;letter-spacing:.2px}
.service p{font-size:6.5px;line-height:10.4px;color:var(--light);margin-top:5px}
.flow-arrow{position:absolute}
.about{position:absolute;top:596px;left:0;width:726px;height:252px;background:var(--gold)}
.about-photo{position:absolute;left:66px;top:28px;width:196px;height:196px;border-radius:50%;border:2px solid #fff;background:radial-gradient(circle at 60% 40%,#3a3530 0%,#6b5e52 40%,#c9c2b8 75%,#e9e4dc 100%)}
.about-copy{position:absolute;left:293px;top:38px;width:350px;color:#fff}
.about-copy h2{font-family:'Raleway',sans-serif;font-weight:500;font-size:12.6px;letter-spacing:.4px}
.about-copy p{font-size:7.2px;line-height:13.6px;margin-top:10px}
.about-copy ul{list-style:none;margin-top:6px}
.about-copy li{font-size:7.2px;line-height:15.5px;padding-left:16px;position:relative}
.about-copy li::before{content:"";position:absolute;left:1px;top:6px;width:4px;height:4px;border-radius:50%;background:#fff}
.locations{position:absolute;top:848px;left:0;width:726px;height:184px}
.locations .section-title{margin-top:32px}
.office{position:absolute;top:106px;display:flex;gap:8px}
.office h4{font-weight:400;font-size:8.8px;color:#444;line-height:10px}
.office p{font-size:6.3px;line-height:10.4px;color:var(--muted);margin-top:5px}
.footer{position:absolute;top:1032px;left:0;width:726px;height:168px;background:var(--footer);color:#fff}
.footer-col{position:absolute;top:29px}
.footer-col h5{font-weight:400;font-size:9.2px;letter-spacing:.3px}
.footer-col ul{list-style:none;margin-top:12px}
.footer-col li{font-size:6.9px;line-height:15px;color:#9a9a9a}
.newsletter p{font-size:6.6px;line-height:12px;color:#9a9a9a;margin-top:12px;width:140px}
.email{width:128px;height:23px;background:#fff;margin-top:10px;font-size:5.5px;color:#aaa;padding:8px 7px}
.subscribe{display:inline-block;margin-top:4px;background:var(--gold);font-size:6.5px;font-weight:500;padding:8px 12px}
.copyright{position:absolute;left:80px;top:141px;font-size:6.5px;color:#9a9a9a}
</style>
</head>
<body>
<div class="page">
  <header class="hero">
    <div class="hero-photo" role="img" aria-label="Two businessmen in suits reviewing documents at a desk"></div>
    <div class="hero-shade"></div>
    <div class="brand"><span class="brand-mark"></span>Tarrow, Quell, Bancroft<br>&amp; Nilsen, LLP</div>
    <nav class="nav">
      <a class="active">HOME</a><a>WHY TQBN?</a><a>SERVICES</a><a>PROFILES</a><a>TIPS &amp; LINKS</a><a>CLIENT LOGIN</a><a>CONTACT</a>
    </nav>
    <div class="hero-copy">
      <h1 class="hero-title">WELCOME TO TQBN</h1>
      <p class="hero-lead">We are an accounting, audit and business management firm with offices in New York City, Long Island, and Florida.</p>
      <p class="hero-body">Our experienced CPA's offer financial solutions and vast resources in all aspects of accounting, tax planning, tax return preparation, personal financial planning, estate and trust, and small business consulting.</p>
      <span class="btn-outline">READ MORE</span>
    </div>
    <svg class="slider-arrows" width="24" height="20" viewBox="0 0 24 20" aria-hidden="true"><path d="M9 2 L2 10 L9 18 M15 2 L22 10 L15 18" fill="none" stroke="#fff" stroke-width="1.2"/></svg>
  </header>

  <section class="services">
    <h2 class="section-title">SERVICES OF <span>TQBN</span></h2>
    <p class="section-intro">Each member of our team is carefully chosen for their expertise, experience &nbsp;and commitment<br>to our profession. TQBN is a tax, audit and business advisory practice with over 30 professionals in NYC and Long Island.</p>

    <div class="service" style="left:85px">
      <div class="service-icon"><svg width="26" height="26" viewBox="0 0 26 26"><rect x="5" y="4" width="15" height="19" rx="1" fill="none" stroke="#e3a20f" stroke-width="1.5"/><rect x="9" y="2" width="7" height="4" fill="#e3a20f"/><path d="M8 10h9M8 14h9M8 18h5" stroke="#e3a20f" stroke-width="1.3"/><circle cx="20" cy="20" r="4" fill="#e3a20f"/></svg></div>
      <h3>ACCOUNTING &amp; AUDITING</h3>
      <p>Lorem ipsum dolor sit amet, elit sed do eiusmod tempor incididunt ut labore veniam nostrud</p>
    </div>
    <div class="service" style="left:229px">
      <div class="service-icon"><svg width="26" height="26" viewBox="0 0 26 26"><rect x="3" y="4" width="20" height="14" rx="1" fill="none" stroke="#e3a20f" stroke-width="1.5"/><circle cx="13" cy="11" r="4" fill="none" stroke="#e3a20f" stroke-width="2.2" stroke-dasharray="2 1.2"/><path d="M9 22h8M13 18v4" stroke="#e3a20f" stroke-width="1.5"/></svg></div>
      <h3>TAX SERVICES</h3>
      <p>Lorem ipsum dolor sit amet, elit sed do eiusmod tempor incididunt ut labore veniam nostrud</p>
    </div>
    <div class="service" style="left:373px">
      <div class="service-icon"><svg width="28" height="26" viewBox="0 0 28 26"><rect x="9" y="3" width="10" height="7" fill="#e3a20f"/><circle cx="6" cy="12" r="2.5" fill="#e3a20f"/><circle cx="22" cy="12" r="2.5" fill="#e3a20f"/><circle cx="14" cy="13" r="2.5" fill="#e3a20f"/><path d="M2 22v-5h8v5M18 22v-5h8v5M10 22v-4h8v4" fill="#e3a20f"/></svg></div>
      <h3>MANAGEMENT CONSULTING</h3>
      <p>Lorem ipsum dolor sit amet, elit sed do eiusmod tempor incididunt ut labore veniam nostrud</p>
    </div>
    <div class="service" style="left:510px">
      <div class="service-icon"><svg width="26" height="26" viewBox="0 0 26 26"><circle cx="10" cy="9" r="4" fill="#e3a20f"/><path d="M3 23c0-6 3-9 7-9s7 3 7 9z" fill="#e3a20f"/><circle cx="19" cy="8" r="5" fill="#fff" stroke="#e3a20f" stroke-width="1.5"/><path d="M19 5v3h2" stroke="#e3a20f" stroke-width="1.2" fill="none"/></svg></div>
      <h3>FINANCIAL PLANNING</h3>
      <p>Lorem ipsum dolor sit amet, elit sed do eiusmod tempor incididunt ut labore veniam nostrud</p>
    </div>

    <svg class="flow-arrow" style="left:200px;top:118px" width="46" height="18" viewBox="0 0 46 18"><path d="M2 12 Q22 -2 42 12" fill="none" stroke="#ddd" stroke-width="3"/><path d="M36 8 L43 13 L35 15" fill="none" stroke="#ddd" stroke-width="3"/></svg>
    <svg class="flow-arrow" style="left:346px;top:142px" width="46" height="18" viewBox="0 0 46 18"><path d="M2 6 Q22 20 42 6" fill="none" stroke="#ddd" stroke-width="3"/><path d="M35 3 L43 5 L38 12" fill="none" stroke="#ddd" stroke-width="3"/></svg>
    <svg class="flow-arrow" style="left:488px;top:118px" width="46" height="18" viewBox="0 0 46 18"><path d="M2 12 Q22 -2 42 12" fill="none" stroke="#ddd" stroke-width="3"/><path d="M36 8 L43 13 L35 15" fill="none" stroke="#ddd" stroke-width="3"/></svg>
  </section>

  <section class="about">
    <div class="about-photo" role="img" aria-label="Overhead view of a person typing on a laptop beside a coffee cup and notes"></div>
    <div class="about-copy">
      <h2>TARROW, QUELL, BANCROFT &amp; NILSEN, LLP</h2>
      <p>Is an accounting, audit and business management firm with offices in New York City, Long Island, and Florida. Our experienced CPA's offer financial solutions and vast resources in all aspects of accounting, tax planning, tax return preparation, personal financial planning, estate and trust, and small business consulting.</p>
      <ul>
        <li>Condominium, Homeowner and Timeshare Association Services/Auditor</li>
        <li>Audit, Review, and Attestation Services</li>
        <li>Accounting and Tax Services</li>
        <li>Non Profit Audits/Auditors</li>
        <li>Grant Audits/Auditors</li>
        <li>Single Audits and OMB 133 Audits/Auditors</li>
        <li>401-K Audits/Auditors</li>
      </ul>
    </div>
  </section>

  <section class="locations">
    <h2 class="section-title">LOCATION <span>TQBN</span></h2>
    <p class="section-intro">Each member of our team is carefully chosen for their expertise, experience &nbsp;and commitment<br>to our profession. TQBN is a tax, audit and business advisory practice with over 30 professionals in NYC and Long Island.</p>

    <div class="office" style="left:78px">
      <svg width="16" height="22" viewBox="0 0 16 22"><path d="M8 1C4 1 1 4 1 8c0 5 7 13 7 13s7-8 7-13c0-4-3-7-7-7z" fill="#e3a20f"/><circle cx="8" cy="8" r="3" fill="#fff"/></svg>
      <div><h4>NEW YORK CITY OFFICE</h4><p>2210 Harbor Row Avenue<br>2nd Floor</p></div>
    </div>
    <div class="office" style="left:235px">
      <svg width="16" height="22" viewBox="0 0 16 22"><path d="M8 1C4 1 1 4 1 8c0 5 7 13 7 13s7-8 7-13c0-4-3-7-7-7z" fill="#e3a20f"/><circle cx="8" cy="8" r="3" fill="#fff"/></svg>
      <div><h4>LONG ISLAND OFFICE</h4><p>48 Cedar Crest Road<br>Elmvale, NY 11990</p></div>
    </div>
    <div class="office" style="left:387px">
      <svg width="16" height="22" viewBox="0 0 16 22"><path d="M8 1C4 1 1 4 1 8c0 5 7 13 7 13s7-8 7-13c0-4-3-7-7-7z" fill="#e3a20f"/><circle cx="8" cy="8" r="3" fill="#fff"/></svg>
      <div><h4>FLORIDA OFFICE</h4><p>740 NW 12th Street, Suite 305<br>Palm Shores, FL 33999</p></div>
    </div>
    <div class="office" style="left:529px">
      <svg width="16" height="22" viewBox="0 0 16 22"><path d="M8 1C4 1 1 4 1 8c0 5 7 13 7 13s7-8 7-13c0-4-3-7-7-7z" fill="#e3a20f"/><circle cx="8" cy="8" r="3" fill="#fff"/></svg>
      <div><h4>HOLLIS BARKER<br>&amp; WENDTFIELD</h4><p>740 NW 12th Street &nbsp;Suite 305<br>Palm Shores, FL 33999</p></div>
    </div>
  </section>

  <footer class="footer">
    <div class="footer-col" style="left:79px"><h5>INFORMATION</h5><ul><li>Home</li><li>About us</li><li>Services</li><li>Clients</li><li>Contact us</li></ul></div>
    <div class="footer-col" style="left:185px"><h5>SERVICES</h5><ul><li>Accounting and Tax Services</li><li>Non Profit Audits/Auditors</li><li>Grant Audits/Auditors</li><li>Single Audits and OMB 133</li><li>Audits/Auditors</li></ul></div>
    <div class="footer-col" style="left:314px"><h5>SUPPORT LINKS</h5><ul><li>Privacy Policy</li><li>Terms &amp; Condition</li><li>Site Map</li></ul></div>
    <div class="footer-col" style="left:420px"><h5>SOCIAL LINKS</h5><ul><li>Friendwall</li><li>Chirpline</li><li>ProNet</li><li>Circles</li><li>ViewTube</li></ul></div>
    <div class="footer-col newsletter" style="left:517px"><h5>NEWSLETTER SIGN UP</h5><p>Lorem ipsum dolor sit amet, consectetur adipiscing elit eiusmod tempor</p><div class="email">Email Address...</div><span class="subscribe">SUBSCRIBE</span></div>
    <p class="copyright">Copyright 2016 trqbnllp . All rights reserved.</p>
  </footer>
</div>
</body>
</html>
```